Postcard Design Project

Company Name - Velmora Office Goods LLC We service and Repair printers, Fax and Copiers and sells all Business Technology supplies including supplies for Printers and Copiers to all NYC Metropolitan area.

Target Market(s)

NYC Small to Medium size business

Industry/Entity Type

Business

Font styles to use
Sans Serif

Colors

Designer to choose colors to be used in the design.

Requirements
Must have
• Printer Repairs and Toners Sales

```html
<!DOCTYPE html>
<html lang="en">
<head>
<meta charset="utf-8">
<title>Velmora Office Goods – Printer Repair Postcard</title>
<link href="https://fonts.googleapis.com/css2?family=Open+Sans:wght@400;600;700;800&display=swap" rel="stylesheet">
<style>
  :root{
    --blue:#00a9e6;
    --head-blue:#1a6fc0;
    --red:#ec1c24;
    --yellow:#fff200;
    --magenta:#e6007e;
    --purple:#6a35a8;
    --ink:#111111;
    --white:#ffffff;
    --silver-1:#f4f4f4;
    --silver-2:#d9d9d9;
  }
  html,body{margin:0;padding:0;overflow:hidden;background:#ffffff;}
  .postcard{
    position:relative;width:960px;height:1200px;overflow:hidden;
    font-family:"Open Sans",sans-serif;color:var(--ink);
    background:var(--white);
  }
  .backdrop{position:absolute;inset:0;}
  .brand{position:absolute;left:76px;top:170px;display:flex;align-items:center;gap:16px;}
  .brand-mark{width:48px;height:48px;background:var(--head-blue);}
  .brand-name{font-weight:700;font-size:40px;color:var(--ink);letter-spacing:-0.5px;}
  .headline{position:absolute;left:48px;top:224px;margin:0;}
  .headline .question{display:block;font-weight:800;font-size:50px;color:var(--head-blue);line-height:58px;}
  .headline .pitch{display:block;font-weight:700;font-size:47px;line-height:52px;color:var(--ink);}
  .services{position:absolute;left:47px;top:436px;color:var(--white);}
  .services h2{margin:0 0 0 7px;font-weight:600;font-size:33px;line-height:44px;color:var(--white);display:inline-block;
    padding-bottom:4px;border-bottom:3px solid var(--ink);position:relative;}
  .services h2::after{content:"";position:absolute;left:0;bottom:-3px;width:40%;height:3px;background:var(--red);}
  .services p{margin:10px 0 0;font-size:26px;line-height:32px;}
  .service-list{list-style:none;margin:0;padding:0;}
  .service-list li{font-size:26px;line-height:32.3px;padding-left:23px;position:relative;}
  .service-list li::before{content:"";position:absolute;left:2px;top:12px;width:8px;height:8px;
    background:conic-gradient(var(--magenta) 0 25%,var(--yellow) 0 50%,var(--ink) 0 75%,var(--blue) 0);transform:rotate(45deg);}
  .supplies{position:absolute;left:37px;top:738px;color:var(--white);font-size:25px;line-height:33px;}
  .supplies strong{color:var(--yellow);font-weight:600;display:block;margin-bottom:2px;}
  .ribbon{position:absolute;left:46px;top:852px;width:482px;height:80px;}
  .ribbon span{position:absolute;inset:0;display:flex;align-items:center;justify-content:center;text-align:center;
    color:var(--white);font-weight:700;font-size:30px;line-height:32px;}
  .call{position:absolute;left:132px;top:948px;width:335px;text-align:center;}
  .call-label{font-weight:700;font-size:36px;line-height:48px;margin:0;}
  .call-icon{display:block;margin:6px auto 0;}
  .phone{position:absolute;left:0;width:600px;top:1072px;text-align:center;font-weight:700;font-size:60px;color:var(--red);letter-spacing:-0.5px;}
  .web{position:absolute;left:0;width:600px;top:1138px;text-align:center;font-size:28px;}
  .web b{font-weight:700;}
</style>
</head>
<body>
<main class="postcard">
  <svg class="backdrop" width="960" height="1200" viewBox="0 0 960 1200">
    <defs>
      <linearGradient id="silver" x1="0" y1="0" x2="1" y2="1">
        <stop offset="0" stop-color="#e9e9e9"/><stop offset="0.45" stop-color="#fbfbfb"/><stop offset="1" stop-color="#d4d4d4"/>
      </linearGradient>
      <linearGradient id="photoTech" x1="0" y1="0" x2="1" y2="1">
        <stop offset="0" stop-color="#c9d3df"/><stop offset="1" stop-color="#5b6574"/>
      </linearGradient>
      <linearGradient id="photoHands" x1="0" y1="0" x2="1" y2="1">
        <stop offset="0" stop-color="#8a8a8a"/><stop offset="1" stop-color="#d8c2b0"/>
      </linearGradient>
      <linearGradient id="photoToner" x1="0" y1="0" x2="1" y2="1">
        <stop offset="0" stop-color="#ffffff"/><stop offset="1" stop-color="#c9c9d2"/>
      </linearGradient>
      <linearGradient id="photoPrinter" x1="0" y1="0" x2="1" y2="1">
        <stop offset="0" stop-color="#eeeeee"/><stop offset="0.5" stop-color="#b8bcc0"/><stop offset="1" stop-color="#e88a5a"/>
      </linearGradient>
    </defs>

    <!-- header -->
    <rect class="header-bg" x="0" y="0" width="960" height="414" fill="url(#silver)"/>
    <g role="img" aria-label="Photo of a smiling technician repairing an office printer">
      <rect x="655" y="170" width="240" height="240" rx="22" transform="rotate(45 775 290)" fill="url(#photoTech)" stroke="var(--purple)" stroke-width="5"/>
    </g>
    <path class="header-divider" d="M0 414 L455 414 Q478 408 482 377 Q486 408 509 414 L960 414" fill="none" stroke="var(--ink)" stroke-width="5"/>

    <!-- blue service panel -->
    <path class="service-panel" d="M0 419 L389 419 Q420 440 434 499 Q470 470 503 476 L680 711 L680 800 Q640 810 615 838 Q600 870 590 895 Q560 900 526 935 L300 1200 L0 1200 Z" fill="var(--blue)" stroke="var(--red)" stroke-width="2"/>
    <polygon points="935,480 960,455 960,740 860,640" fill="var(--yellow)"/>

    <g role="img" aria-label="Photo of toner cartridges in four colours">
      <rect x="716" y="375" width="176" height="176" rx="16" transform="rotate(45 804 463)" fill="url(#photoToner)" stroke="var(--magenta)" stroke-width="3"/>
    </g>
    <g role="img" aria-label="Photo of hands servicing the inside of a printer">
      <rect x="517" y="497" width="226" height="226" rx="24" transform="rotate(45 630 610)" fill="url(#photoHands)" stroke="var(--ink)" stroke-width="5"/>
    </g>
    <g role="img" aria-label="Photo of a printer fuser maintenance kit with rollers">
      <rect x="732" y="675" width="176" height="176" rx="16" transform="rotate(45 820 763)" fill="url(#photoToner)" stroke="var(--blue)" stroke-width="3"/>
    </g>

    <!-- call panel -->
    <path class="call-panel" d="M0 1093 L132 985 Q150 972 152 950 Q156 930 178 930 L420 930 Q462 930 465 955 Q470 982 492 988 L580 1070 L960 1070 L960 1200 L0 1200 Z" fill="url(#silver)"/>
    <path d="M0 1093 L132 985 Q150 972 152 950 Q156 930 178 930 L420 930 Q462 930 465 955 Q470 982 492 988 L560 1052" fill="none" stroke="var(--purple)" stroke-width="5"/>
    <path d="M0 1175 L28 1200" stroke="var(--purple)" stroke-width="5"/>

    <rect role="img" aria-label="Photo of an inkjet printer printing a rainbow ribbon of colour" x="524" y="861" width="404" height="339" fill="url(#photoPrinter)"/>

    <!-- ribbon -->
    <polygon points="46,852 528,852 516,891 528,932 46,932 58,891" fill="var(--red)"/>
  </svg>

  <div class="brand">
    <span class="brand-mark"></span>
    <span class="brand-name">Velmora Office Goods</span>
  </div>

  <h1 class="headline">
    <span class="question">GOT DIRTY PRINTER?</span>
    <span class="pitch">Have a Technician<br>in your office today!</span>
  </h1>

  <section class="services">
    <h2>What we Do?</h2>
    <p>Repairing of all kinds of</p>
    <ul class="service-list">
      <li>Laser printers</li>
      <li>Fax &amp; Copiers</li>
      <li>Paper Jams</li>
      <li>Fuser Errors</li>
      <li>Paper crimping</li>
      <li>Cleaning and much more...</li>
    </ul>
  </section>

  <div class="supplies">
    <strong>Save On All your printing supplies like</strong>
    Toners. Drums, Fuser and Maintenance kits.<br>
    Instant Discount and monthly rebates.
  </div>

  <div class="ribbon"><span>SERVICE CONTRACTS<br>AVAILABLE</span></div>

  <div class="call">
    <p class="call-label">CALL NOW</p>
    <svg class="call-icon" width="80" height="80" viewBox="0 0 80 80" aria-hidden="true">
      <circle cx="40" cy="40" r="35" fill="none" stroke="var(--ink)" stroke-width="5"/>
      <path d="M27 23 l8 0 l3 10 l-5 4 q4 9 12 13 l4 -5 l10 3 l0 8 q-2 4 -7 4 q-30 -4 -31 -31 q0 -5 6 -6z" fill="var(--ink)"/>
      <path d="M45 26 q9 2 11 11 M46 18 q15 3 18 18" fill="none" stroke="var(--ink)" stroke-width="3" stroke-linecap="round"/>
    </svg>
  </div>

  <div class="phone">718-555-0142</div>
  <div class="web">www.<b>velmoragoods</b>.com</div>
</main>
</body>
</html>
```